Plumbing Business Card Design

our business is a plumbing business.
we would like to see designs with our LOGO featured and then either purple or black writing with a white back ground
or black back ground with white or purple writing or even a purple card!
one option we would love to see is if you could get the TKR letters away from the white background ( it is currently in a white box as a jpeg )it is currently on and overlay it onto black.
FRONT
TKR image to be displayed on the front, please use the attached picture. ( you can remove the email address and mobile number from the botttom and re write it in different font or in a different place on the front.
Directly under the large TKR we would like the words Tidewell Kern Plumbing.
could be spread out like this T I D E W E L L K E R N
P L U M B I N G
We really are open to suggestions though!
Also on the front of the card we could like our little catch phrase somewhere Brindle's Local Plumber

we dont want in plumbing pictures or photos but we are open to swirl across the card or water movement or droplets.

BACK
These services need to be dot pointed or listed on the back
Hot & Cold Water Services
Gas Fitting
Bathroom & Kitchen Renovations
Metal Roofing & Guttering
New Homes & Extensions
Hot Water Service Changeovers
Drainage & Stormwater Works
All General Plumbing & Maitenance

in smaller writing or down the bottom of the card on the back please display write this Lic. No 473918

Contact Information for Business Card

Colm Kern
Mobile: 0427 391 206
email: tidewellkernplumbing@mailnest.example
FInd Us on Tidewell Kern Plumbing (plain square in place of the network mark) Tidewell Kern Plumbing ( with the f symbol ) either on the front or the back

```html
<!DOCTYPE html>
<html lang="en">
<head>
<meta charset="utf-8">
<title>Tidewell Kern Plumbing – Business Card</title>
<link rel="stylesheet" href="https://fonts.googleapis.com/css2?family=Source+Sans+3:wght@400;600;700;800&display=swap">
<style>
  :root {
    --backdrop: #9b9b9b;
    --card-white: #f0eff3;
    --brand-purple: #5a1fc4;
    --brand-purple-text: #5c22c8;
    --ink: #2e2a36;
    --on-purple: #f4f1fb;
    --faint-mark: rgba(120, 80, 210, 0.16);
  }
  * { box-sizing: border-box; margin: 0; padding: 0; }
  html, body { width: 1105px; height: 1200px; overflow: hidden; }
  body {
    background: var(--backdrop);
    font-family: "Source Sans 3", "Myriad Pro", Arial, sans-serif;
    position: relative;
  }
  .card {
    position: absolute;
    left: 182px;
    width: 746px;
    height: 425px;
    overflow: hidden;
  }
  .card--front { top: 119px; background: var(--card-white); }
  .card--back { top: 637px; background: var(--brand-purple); }

  .wordmark {
    position: absolute;
    font-weight: 800;
    font-size: 124px;
    line-height: 1;
    letter-spacing: 6px;
    white-space: nowrap;
  }
  .tagline {
    position: absolute;
    font-weight: 700;
    font-size: 17px;
    letter-spacing: 2.6px;
    white-space: nowrap;
  }

  .card--front .wordmark { left: 52px; top: 52px; color: var(--brand-purple-text); }
  .card--front .tagline { left: 56px; top: 184px; color: var(--brand-purple-text); }
  .contact-name {
    position: absolute; left: 55px; top: 228px;
    font-size: 28px; font-weight: 600; color: var(--brand-purple-text);
  }
  .contact-list { position: absolute; left: 55px; top: 284px; list-style: none; }
  .contact-list li {
    display: flex; align-items: center; gap: 10px;
    font-size: 20px; color: var(--ink); height: 29px; white-space: nowrap;
  }
  .contact-icon { width: 17px; height: 17px; flex: none; }
  .social-square { width: 15px; height: 15px; background: var(--brand-purple-text); flex: none; margin-left: 1px; }

  .faint-mark {
    position: absolute; left: 656px; top: 205px;
    transform: translate(-50%, -50%) rotate(90deg);
    font-weight: 800; font-size: 178px; line-height: 1;
    letter-spacing: 22px; color: var(--faint-mark);
    white-space: nowrap;
  }

  .card--back .wordmark { left: 52px; top: 124px; color: var(--on-purple); }
  .card--back .tagline { left: 56px; top: 266px; color: var(--on-purple); }
  .licence {
    position: absolute; left: 122px; top: 302px;
    font-size: 17px; color: var(--on-purple); white-space: nowrap;
  }
  .catchphrase {
    position: absolute; left: 56px; width: 274px; top: 338px;
    text-align: center; font-size: 17px; font-style: normal; font-weight: 600;
    color: var(--on-purple); white-space: nowrap;
  }
  .service-list {
    position: absolute; left: 364px; top: 84px; list-style: none;
  }
  .service-list li {
    font-size: 20px; color: var(--on-purple); height: 32.7px;
    padding-left: 14px; position: relative; white-space: nowrap;
  }
  .service-list li::before {
    content: "•"; position: absolute; left: 0; top: 0;
  }
</style>
</head>
<body>
  <section class="card card--front" aria-label="Business card front">
    <div class="faint-mark" aria-hidden="true">TKR</div>
    <div class="wordmark">TKR</div>
    <div class="tagline">TIDEWELL &nbsp;KERN &nbsp;PLUMBING</div>
    <div class="contact-name">Colm Kern</div>
    <ul class="contact-list">
      <li>
        <svg class="contact-icon" viewBox="0 0 17 17" aria-hidden="true">
          <rect x="4" y="1" width="9" height="15" rx="1.6" fill="none" stroke="#5c22c8" stroke-width="1.8"/>
          <line x1="7" y1="13.2" x2="10" y2="13.2" stroke="#5c22c8" stroke-width="1.5"/>
        </svg>
        0427 391 206
      </li>
      <li>
        <svg class="contact-icon" viewBox="0 0 17 17" aria-hidden="true">
          <rect x="1.5" y="4" width="14" height="10" fill="none" stroke="#5c22c8" stroke-width="1.6"/>
          <polyline points="1.5,4 8.5,10 15.5,4" fill="none" stroke="#5c22c8" stroke-width="1.6"/>
        </svg>
        tidewellkernplumbing@mailnest.example
      </li>
      <li>
        <span class="social-square" aria-hidden="true"></span>
        Tidewell Kern Plumbing
      </li>
    </ul>
  </section>

  <section class="card card--back" aria-label="Business card back">
    <div class="wordmark">TKR</div>
    <div class="tagline">TIDEWELL &nbsp;KERN &nbsp;PLUMBING</div>
    <div class="licence">Lic. No 473918</div>
    <p class="catchphrase">Brindle's Local Plumber</p>
    <ul class="service-list">
      <li>Hot &amp; Cold Water Services</li>
      <li>Gas Fitting</li>
      <li>Bathroom &amp; Kitchen Renovations</li>
      <li>Metal Roofing &amp; Guttering</li>
      <li>New Homes &amp; Extensions</li>
      <li>Hot Water Service Changeovers</li>
      <li>Drainage &amp; Stormwater Works</li>
      <li>All General Plumbing &amp; Maitenance</li>
    </ul>
  </section>
</body>
</html>
```